KTM Inquiry Partners PLLC
Law Firm Conducting Investigations
KTM Inquiry Partners PLLC -
Creative Brief
Professional
Dale Morrow
Attorney
21430 SW 3rd Ave, Suite C2-418 Bellevue, WA 98006
dale@ktminquiry-example.com
www.ktminquiry-example.com
I would like the card to be simple, clean and professional. Please use color schemes that match the logo, but don't use too much gold.
The back of the card should be blank.

```html
<!DOCTYPE html>
<html lang="en">
<head>
<meta charset="utf-8">
<title>KTM Inquiry Partners PLLC – Business Card</title>
<link href="https://fonts.googleapis.com/css2?family=Arimo:wght@400;700&display=swap" rel="stylesheet">
<style>
  :root {
    --gold: #9b7a22;
    --gold-dark: #6e500e;
    --gold-light: #ecd78f;
    --ink: #2b2b2b;
    --mark: #3a2c12;
    --paper-top: #ffffff;
    --paper-bottom: #e3e4e6;
    --rule: #333333;
  }
  * { margin: 0; padding: 0; box-sizing: border-box; }
  html, body { width: 1200px; height: 689px; overflow: hidden; background: #ffffff; }
  .card {
    position: relative;
    width: 1200px;
    height: 689px;
    overflow: hidden;
    font-family: "Arimo", Arial, sans-serif;
    color: var(--ink);
    background: linear-gradient(180deg, var(--paper-top) 20%, var(--paper-bottom) 100%);
  }
  .gold-band {
    position: absolute;
    left: 0; top: 0;
    width: 1200px; height: 92px;
    background: linear-gradient(90deg, var(--gold-dark) 0%, #b8963f 30%, var(--gold-light) 55%, #c9a955 80%, var(--gold-dark) 100%);
  }
  .brand-square {
    position: absolute;
    left: 70px; top: 60px;
    width: 150px; height: 150px;
    background: var(--mark);
  }
  .brand-rule {
    position: absolute;
    left: 276px; top: 40px;
    width: 3px; height: 250px;
    background: var(--rule);
  }
  .brand-name {
    position: absolute;
    left: 306px; top: 108px;
    font-weight: 700;
    font-size: 58px;
    line-height: 1.1;
    letter-spacing: 1px;
    color: var(--gold);
  }
  .person {
    position: absolute;
    left: 298px; top: 336px;
    font-size: 40px;
    color: var(--ink);
  }
  .person .name { font-weight: 700; color: var(--gold); }
  .person .divider { font-weight: 700; color: var(--gold); }
  .contact {
    position: absolute;
    left: 300px; top: 488px;
    font-size: 27px;
    line-height: 40px;
    list-style: none;
  }
  .contact .label { font-weight: 700; color: var(--gold); }
  .website {
    position: absolute;
    right: 42px; top: 608px;
    font-size: 27px;
    font-weight: 700;
    color: var(--gold);
  }
</style>
</head>
<body>
  <div class="card">
    <div class="gold-band"></div>
    <div class="brand-square"></div>
    <div class="brand-rule"></div>
    <div class="brand-name">KTM Inquiry<br>Partners</div>

    <p class="person"><span class="name">Dale Morrow</span> <span class="divider">|</span> Attorney</p>

    <ul class="contact">
      <li><span class="label">P:</span> 425-555-0193</li>
      <li><span class="label">E:</span> dale@ktminquiry-example.com</li>
      <li><span class="label">A:</span> 21430 SW 3rd Ave,<br>Suite C2-418 Bellevue, WA 98006</li>
    </ul>

    <p class="website">www.ktminquiry-example.com</p>
  </div>
</body>
</html>
```